Nebelkreis - needs a CD/Cover Design for a VA Compilation

We need a CD-Design/Cover-Artwork for our Various Artists Compilation called 'Nebelkreis', which means "Fog circle". Back then our events were based in one of Germanys best underground techno-clubs., which we also called "our temple".
The artists featured on this compilation rather performed at our events or had a massive influence on the music the djs played.
The sound is glitchy, technically detailed and a little unpredictable.

We would like to see some designs not too colourful!

Target Market(s)

complex electronic music listeners

Industry/Entity Type

Club

Font styles to use
Sans Serif

Colors
ec1f27

Requirements
Must have
• Ideally the artwork should be something otherworldly, abstract/glitchy, be an optical illusion and/or have geometric complexity.
Nice to have
• - probably black and white design fits better with us, but you can also try it with a very few colors.
- maybe something futuristic or scatchy
Should not have
• - it should definitely NOT be too colourful.
- no humans!! or animals
- in case you think to draw a temple, please use it more abstract, nothing too obviously, we dont wanna look like a hippie event!
- no musical notes
- no obvious "play" symbol / headphones or vinyl images

```html
<!DOCTYPE html>
<html lang="en">
<head>
<meta charset="utf-8">
<title>Nebelkreis – Various Artists Compilation</title>
<link rel="stylesheet" href="https://fonts.googleapis.com/css2?family=Jura:wght@300;500&display=swap">
<style>
  :root {
    --paper: #ffffff;
    --ink-black: #050203;
    --deep-red: #3a0508;
    --mid-red: #7a0d12;
    --hot-red: #a3141b;
    --brand-red: #ec1f27;
    --hub-white: #f2f2f2;
    --hub-grey: #c9c9c9;
  }
  * { margin: 0; padding: 0; box-sizing: border-box; }
  html, body {
    width: 1200px;
    height: 762px;
    overflow: hidden;
    background: var(--paper);
  }
  .canvas {
    position: relative;
    width: 1200px;
    height: 762px;
    background: var(--paper);
  }

  /* Front cover */
  .cover {
    position: absolute;
    left: 40px;
    top: 81px;
    width: 600px;
    height: 600px;
    overflow: hidden;
    background: var(--ink-black);
  }
  .cover-artwork {
    position: absolute;
    inset: 0;
    background:
      linear-gradient(128deg, transparent 38%, rgba(163, 20, 27, 0.35) 46%, transparent 54%),
      linear-gradient(135deg, transparent 55%, rgba(122, 13, 18, 0.3) 62%, transparent 70%),
      radial-gradient(ellipse 40% 30% at 42% 62%, var(--hot-red) 0%, var(--mid-red) 25%, var(--deep-red) 55%, transparent 85%),
      radial-gradient(ellipse 35% 40% at 30% 30%, rgba(122, 13, 18, 0.55) 0%, transparent 75%),
      radial-gradient(ellipse 30% 25% at 75% 22%, rgba(122, 13, 18, 0.45) 0%, transparent 75%),
      linear-gradient(180deg, #140304 0%, var(--ink-black) 70%, #000000 100%);
  }
  .cover-title {
    position: absolute;
    right: 28px;
    bottom: 74px;
    font-family: 'Jura', sans-serif;
    font-weight: 500;
    font-size: 38px;
    letter-spacing: 4px;
    margin-right: -4px;
    color: var(--brand-red);
    line-height: 1;
  }
  .cover-subtitle {
    position: absolute;
    right: 28px;
    bottom: 40px;
    font-family: 'Jura', sans-serif;
    font-weight: 300;
    font-size: 19px;
    color: var(--brand-red);
    line-height: 1;
  }

  /* Disc label */
  .disc {
    position: absolute;
    left: 662px;
    top: 123px;
    width: 516px;
    height: 516px;
  }
  .disc svg { display: block; }
  .disc-title {
    position: absolute;
    left: 356px;
    top: 236px;
    font-family: 'Jura', sans-serif;
    font-weight: 500;
    font-size: 19px;
    letter-spacing: 2px;
    color: var(--brand-red);
    line-height: 1;
  }
</style>
</head>
<body>
<main class="canvas">

  <section class="cover">
    <div class="cover-artwork" role="img" aria-label="Abstract glitchy artwork of red and black fractal streaks and sweeping curves"></div>
    <h1 class="cover-title">NEBELKREIS</h1>
    <p class="cover-subtitle">VARIOUS ARTISTS COMPILATION</p>
  </section>

  <section class="disc">
    <svg width="516" height="516" viewBox="0 0 516 516">
      <defs>
        <radialGradient id="disc-art" cx="40%" cy="58%" r="62%">
          <stop offset="0%" stop-color="#a3141b"/>
          <stop offset="22%" stop-color="#7a0d12"/>
          <stop offset="50%" stop-color="#3a0508"/>
          <stop offset="100%" stop-color="#050203"/>
        </radialGradient>
        <linearGradient id="disc-sweep" x1="0" y1="1" x2="1" y2="0">
          <stop offset="0.4" stop-color="#a3141b" stop-opacity="0"/>
          <stop offset="0.5" stop-color="#a3141b" stop-opacity="0.35"/>
          <stop offset="0.6" stop-color="#a3141b" stop-opacity="0"/>
        </linearGradient>
      </defs>
      <g role="img" aria-label="Abstract red and black streak artwork on the disc label">
        <circle cx="258" cy="258" r="258" fill="url(#disc-art)"/>
        <circle cx="258" cy="258" r="258" fill="url(#disc-sweep)"/>
      </g>
      <circle cx="258" cy="258" r="72" fill="var(--hub-white)" stroke="var(--hub-grey)" stroke-width="1.5"/>
      <circle cx="258" cy="258" r="36" fill="none" stroke="var(--hub-grey)" stroke-width="3"/>
      <circle cx="258" cy="258" r="30" fill="var(--paper)" stroke="#9a9a9a" stroke-width="1"/>
    </svg>
    <p class="disc-title">NEBELKREIS</p>
  </section>

</main>
</body>
</html>
```